Double sided business card design for Vantor 2012 - Logo already done

Double sided business card that uses the EPS vector logo we''ve already had designed (files attached).

Target Market(s)

15, 18, 21 and over 30

Industry/Entity Type

Business

Requirements
Must have
• The same color writting as the design on the logo
Nice to have
• Company name: Taloven Showcase 2019
• Full Name:         Mr D.Oblesky
•                          Ferrow Lane
•                          Hertfordshire
•                          KM19 3PL
•                          England

• Choices between the different versions.
Should not have
• Anything offensive.

```html
<!DOCTYPE html>
<html lang="en">
<head>
<meta charset="utf-8">
<title>Taloven Showcase 2019 – Business Card, Version 1</title>
<link href="https://fonts.googleapis.com/css2?family=Cinzel:wght@400;600&family=Marcellus&family=Source+Sans+3:wght@400&display=swap" rel="stylesheet">
<style>
  :root {
    --page-bg: #ffffff;
    --label-ink: #111111;
    --card-bg: #000000;
    --card-ink: #ffffff;
    --glow-teal: #5fe8d6;
    --glow-cyan: #2fd0f0;
  }
  * { margin: 0; padding: 0; box-sizing: border-box; }
  html, body {
    width: 684px; height: 1200px; overflow: hidden;
    background: var(--page-bg);
  }
  .sheet { position: relative; width: 684px; height: 1200px; }
  .sheet-label {
    position: absolute; left: 0; width: 684px; text-align: center;
    font-family: "Source Sans 3", sans-serif; font-size: 25px;
    color: var(--label-ink); line-height: 1;
  }
  .label-version { top: 44px; }
  .label-front { top: 542px; }
  .label-back { top: 1133px; }

  .card {
    position: absolute; left: 73px; width: 526px; height: 300px;
    background: var(--card-bg); color: var(--card-ink);
  }
  .card-front { top: 154px; }
  .card-back { top: 729px; }

  .front-name {
    position: absolute; left: 0; top: 70px; width: 526px; text-align: center;
    font-family: "Cinzel", serif; font-weight: 400; font-size: 84px;
    line-height: 1; letter-spacing: 1px;
  }
  .front-company {
    position: absolute; left: 0; top: 208px; width: 526px; text-align: center;
    font-family: "Cinzel", serif; font-weight: 600; font-size: 23px; line-height: 1;
    padding-left: 18px;
  }
  .front-tagline {
    position: absolute; left: 0; top: 234px; width: 526px; text-align: center;
    font-family: "Marcellus", serif; font-style: italic; font-size: 16px;
    letter-spacing: 0.5px; line-height: 1; padding-left: 18px;
  }

  .back-mark {
    position: absolute; left: 66px; top: 46px; width: 140px; text-align: center;
  }
  .back-mark-dot {
    display: block; width: 110px; height: 110px; margin: 0 auto 14px;
    border-radius: 50%;
    background: radial-gradient(circle at 45% 40%, var(--glow-teal), var(--glow-cyan) 70%, #0a5e6e);
  }
  .back-mark-name {
    font-family: "Cinzel", serif; font-weight: 600; font-size: 20px;
    letter-spacing: 1px; line-height: 1;
  }

  .contact {
    position: absolute; left: 226px; top: 71px; width: 260px;
    list-style: none; text-align: center;
    font-family: "Cinzel", serif; font-weight: 600; line-height: 1;
  }
  .contact li { font-size: 25px; height: 31.5px; }
  .contact .contact-person { font-size: 29px; height: 33px; }
  .postcode { word-spacing: 12px; }
</style>
</head>
<body>
<main class="sheet">
  <p class="sheet-label label-version">Version 1</p>

  <section class="card card-front" aria-label="Card front">
    <h1 class="front-name">TALOVEN</h1>
    <p class="front-company">SHOWCASE 2019</p>
    <p class="front-tagline">ONE NIGHT ONLY</p>
  </section>

  <p class="sheet-label label-front">Front</p>

  <section class="card card-back" aria-label="Card back">
    <div class="back-mark">
      <span class="back-mark-dot"></span>
      <p class="back-mark-name">TALOVEN</p>
    </div>
    <ul class="contact">
      <li class="contact-person">Mr. D. Oblesky</li>
      <li>Ferrow Lane</li>
      <li>Hertfordshire</li>
      <li class="postcode">KM19 3PL</li>
      <li>England</li>
    </ul>
  </section>

  <p class="sheet-label label-back">Back</p>
</main>
</body>
</html>
```